Energy and Environment Venture Capital Blog

Look for an out of the box creative design!

I am working on putting together a new blog / website with a few colleagues in the cleantech / energy venture capital space. I would like to push the box on design and get really creative for how to display the following (very simple):

1) Updated News on venture capital and cleantech (rss feed)
2) Would also like to have a profile page to feature "company of the month"
2.1) Included in this page I would like to be able to have a gallery of photos and have it be an interactive profile of company that includes:
2.1.1) Funding received to date, funders, location, founders (really good example of this is would be on greenmark.net. (there may even be a way to take the date right from their website)
EXTRA: would be amazing to be able to place all the selected company on a map
3) Blog entries that can include photos and movies and active commenting
4) Resources section for interesting websites, books, surveys etc. (pagepile)
5) Would like to be able to link my social media (chirpr, friendwall)

A couple good examples include:

http://www.blufinch.co.uk/
http://www.harvestloomworks.co.uk/
http://www.pine-quill.com/

Note: I have a logo designed for the website that I can send across. I also have a domain name registered at http://k7ledgering.com/

I have also attached the draft logo to show the colors I am hoping to use across the site.
Updates

Reason: Really want to make sure that we get the design right and dont want to have to rush things. If however I find a design concept I like I am happy to pull the trigger right away and work outside the contest.

Target Market(s)

venture capitalists, technologists, SMEs

Industry/Entity Type

Venture Capital

Requirements
Must have
• A funky and creative landing page
The profile page (I would like it to be called K7 Profiles) should be the feature section of the website
Nice to have
• What I was hoping to do (if possible) was to create a stock index that tracks some of the leading cleantech stocks on the market. Done know if there is anything out there that is open source but if there is I would love a section on the blog called "K7 Index"
Should not have
• The design should not use old-style, serif fonts like Times New Roman.

```html
<!DOCTYPE html>
<html lang="en">
<head>
<meta charset="utf-8">
<title>k7ledger – All about Energy Venture Capital</title>
<link rel="stylesheet" href="https://fonts.googleapis.com/css2?family=Arimo:wght@400;700&family=Open+Sans:wght@400;600&family=Ubuntu:ital,wght@1,700&display=swap">
<style>
:root{
  --green:#6a9a1f;
  --pill:#a6c77a;
  --pill-edge:#dfe9cf;
  --white:#ffffff;
  --page:#efefef;
  --card-edge:#c9c9c9;
  --ink:#333333;
  --link:#3311cc;
}
*{box-sizing:border-box;margin:0;padding:0}
html,body{width:1200px;height:947px;overflow:hidden}
body{position:relative;background:var(--page);font-family:Arimo,Arial,sans-serif;color:var(--ink)}
a{color:inherit;text-decoration:none}

/* header */
.topbar{position:absolute;left:0;top:0;width:1200px;height:83px;background:var(--green)}
.brand-tab{position:absolute;left:317px;top:-4px;width:166px;height:77px;background:var(--white);border:3px solid #d8d8d8;border-top:none;border-radius:0 0 12px 12px;display:flex;align-items:center;justify-content:center;box-shadow:0 2px 3px rgba(0,0,0,.25)}
.wordmark{font-family:Arimo,Arial,sans-serif;font-weight:700;color:var(--ink);letter-spacing:0;display:flex;align-items:center;line-height:1}
.brand-tab .wordmark{font-size:22px}
.utility{position:absolute;top:18px;left:734px;display:flex;gap:12px;font-family:"Open Sans",sans-serif;font-size:7.5px;color:#fff}
.social-top{position:absolute;top:17px;left:843px;display:flex;gap:4px}
.social-top span,.follow span{width:10px;height:10px;background:#fff;display:block;border-radius:1px}
.nav{position:absolute;top:46px;left:555px;display:flex;gap:6px}
.nav a{width:78px;height:30px;border-radius:15px;background:var(--pill);border:2px solid var(--pill-edge);color:#fff;font-family:"Open Sans",sans-serif;font-weight:600;font-size:9px;display:flex;align-items:center;justify-content:center;gap:6px}
.nav a i{width:12px;height:10px;background:#fff;opacity:.85;border-radius:2px;display:block}

/* hero */
.hero{position:absolute;left:0;top:83px;width:1200px;height:162px;background:var(--white);text-align:center}
.hero .wordmark{position:absolute;left:0;right:0;top:50px;justify-content:center;font-size:40px}
.tagline{position:absolute;left:0;right:0;top:116px;font-family:Ubuntu,sans-serif;font-style:italic;font-weight:700;font-size:22px;color:#333}

/* cards */
.card{position:absolute;width:278px;height:254px;background:var(--white);border:2px solid var(--card-edge);border-radius:16px}
.card h2{position:absolute;left:17px;top:15px;font-size:18px;font-weight:700;color:#333}
.dots{position:absolute;right:16px;top:19px;display:flex;gap:2px}
.dots i{width:9px;height:9px;border-radius:50%;border:1px solid #999;display:block}
.dots i.on{background:var(--link);border-color:var(--link)}
.more{position:absolute;font-size:8px;font-weight:700;color:var(--link)}
.news{position:absolute;left:17px;top:56px;width:254px;font-size:7.2px;line-height:10.8px;color:#333}
.news dt{font-weight:700;margin-top:7px}
.news dt:first-child{margin-top:0}
.news b{color:var(--link)}
.com .wordmark{position:absolute;left:0;right:0;top:76px;justify-content:center;font-size:34px}
.fill{position:absolute;border:1px solid #999}
.post{position:absolute;left:19px;width:240px;font-size:6px;color:#333}
.post .badge{position:absolute;left:0;top:0;width:22px;height:20px;border:1px solid #999;border-radius:2px;background:#fff}
.post .badge::after{content:"";position:absolute;left:6px;top:5px;width:9px;height:9px;background:#555}
.post .who{position:absolute;left:28px;top:5px;font-size:5px;color:#555}
.post .who b{font-size:7.5px;color:#333}
.post .ago{position:absolute;right:0;top:6px;font-size:5.5px}
.post .thumb{top:27px;left:0;width:83px;height:45px}
.post p{position:absolute;left:89px;top:27px;width:148px;font-size:6px;line-height:8.3px;height:33px;overflow:hidden}
.post .meta{position:absolute;left:89px;top:61px;width:148px;font-size:5.8px;display:flex;justify-content:space-between}
.post .meta em{font-style:normal;border:1px solid #888;padding:0 3px;margin-left:8px}
.read{position:absolute;left:17px;width:244px}
.read .thumb{left:0;top:0;width:75px;height:69px;border:2px solid #999}
.read h3{position:absolute;left:82px;top:2px;font-size:7px}
.read p{position:absolute;left:82px;top:16px;width:162px;font-size:5.8px;line-height:7.3px}
.read .see{position:absolute;right:0;top:63px;font-size:6px;color:var(--link)}

/* footer */
.footer{position:absolute;left:0;top:826px;width:1200px;height:121px;background:linear-gradient(#646464 0,#666 40px,#d9d9d9 110px,#eee 121px)}
.foot-links{position:absolute;left:318px;top:28px;display:flex;gap:12px;font-family:"Open Sans",sans-serif;font-size:7.5px;color:#fff}
.follow{position:absolute;left:822px;top:29px;font-family:"Open Sans",sans-serif;font-size:7px;color:#fff}
.follow div{display:flex;gap:3px;margin-top:4px}
.foot-tab{position:absolute;left:529px;top:66px;width:175px;height:60px;background:var(--white);border:1px solid #ccc;border-radius:10px 10px 0 0;text-align:center}
.foot-tab .wordmark{justify-content:center;font-size:20px;margin-top:12px}
.foot-tab small{display:block;font-size:6px;color:#333;margin-top:9px}
</style>
</head>
<body>

<header class="topbar">
  <a class="brand-tab" href="#"><span class="wordmark">k7ledger</span></a>
  <nav class="utility"><a href="#">About us</a><a href="#">Contact</a><a href="#">Blog</a></nav>
  <div class="social-top" aria-label="Social links"><span></span><span></span><span></span></div>
  <nav class="nav">
    <a href="#"><i></i>Home</a>
    <a href="#"><i></i>Profiles</a>
    <a href="#"><i></i>Forums</a>
    <a href="#"><i></i>Advisory</a>
  </nav>
</header>

<section class="hero">
  <div class="wordmark">k7ledger</div>
  <h1 class="tagline">All about Energy Venture Capital</h1>
</section>

<section class="card" style="left:317px;top:266px">
  <h2>News Feed</h2>
  <div class="dots"><i class="on"></i><i></i><i></i></div>
  <dl class="news">
    <dt>Jan 6, 2013</dt>
    <dd><b>SPARK Accelerator</b> received $1,200,000 from an undisclosed investor<br>Growth EquityPoint</dd>
    <dt>Jan 5, 2013</dt>
    <dd><b>HL Group</b> merged with <b>Nordvik Assurance (NVA)</b> for an Undisclosed Amount<br>NVA Kelta's parent company NVA and the HL Group are to merge into a new global entity, NVA HL Group, which should position it as a leading expert in the renewable energy and power sectors, among others.<br>Source</dd>
    <dt>Jan 4, 2013</dt>
    <dd><b>Solva Wireless</b> received an Undisclosed Amount from Corin Systems and QRX Semiconductor<br>TransportationSeries ASource</dd>
  </dl>
  <a class="more" href="#" style="left:200px;top:232px">View All News</a>
</section>

<section class="card com" style="left:605px;top:266px">
  <h2>Company of the Month</h2>
  <div class="wordmark">k7ledger</div>
  <div class="fill" role="img" aria-label="Street map showing the company location" style="left:22px;top:137px;width:232px;height:70px;background:linear-gradient(135deg,#ece8df,#d9d4c8)"></div>
  <a class="more" href="#" style="left:199px;top:232px">View Profile</a>
</section>

<section class="card" style="left:317px;top:538px">
  <h2>Blog Entries</h2>
  <div class="dots"><i class="on"></i><i></i><i></i></div>
  <article class="post" style="top:49px">
    <span class="badge"></span>
    <span class="who"><b>Company</b> Uploaded Image</span>
    <span class="ago">2 Minutes ago</span>
    <div class="fill thumb" role="img" aria-label="Young green plant leaves" style="background:radial-gradient(circle at 50% 40%,#8cc63f,#d6eab8 70%,#fff)"></div>
    <p>NVA Kelta's parent company NVA and the HL Group are to merge into a new global entity, NVA HL Group, which should position it as a leading expert in the</p>
    <div class="meta"><span>Comments<em>30</em></span><span>View All</span></div>
  </article>
  <article class="post" style="top:143px">
    <span class="badge"></span>
    <span class="who"><b>Company</b> Uploaded Video</span>
    <span class="ago">2 Minutes ago</span>
    <div class="fill thumb" role="img" aria-label="Seedling growing from a pile of coins" style="background:linear-gradient(#f4f6ee,#b8a07a 60%,#6b4a2a)"></div>
    <p>NVA Kelta's parent company NVA and the HL Group are to merge into a new global entity, NVA HL Group, which should position it as a leading expert in the</p>
    <div class="meta"><span>Comments<em>30</em></span><span>View All</span></div>
  </article>
  <a class="more" href="#" style="left:211px;top:230px">View All</a>
</section>

<section class="card" style="left:605px;top:538px">
  <h2>Good Reads</h2>
  <div class="dots"><i class="on"></i><i></i><i></i></div>
  <article class="read" style="top:47px">
    <div class="fill thumb" role="img" aria-label="Close-up of stacked coins" style="background:linear-gradient(#7a5a3a,#c8a47a 45%,#f3ebe0)"></div>
    <h3>Book</h3>
    <p>Lorem ipsum dolor sit amet, consectetuer adipiscing elit, sed diam nonummy nibh euismod tincidunt ut laoreet dolore magna aliquam erat volutpat. Ut wisi enim ad minim veniam, quis nostrud exerci tation ullamcorper suscipit lobortis nisl ut aliquip ex ea commodo consequat.</p>
    <a class="see" href="#">See more</a>
  </article>
  <article class="read" style="top:141px">
    <div class="fill thumb" role="img" aria-label="Hand holding coins with a sprouting plant" style="background:linear-gradient(#ffffff,#e6ead8 50%,#c9a57a)"></div>
    <h3>Web Site</h3>
    <p>Lorem ipsum dolor sit amet, consectetuer adipiscing elit, sed diam nonummy nibh euismod tincidunt ut laoreet dolore magna aliquam erat volutpat. Ut wisi enim ad minim veniam, quis nostrud exerci tation ullamcorper suscipit lobortis nisl ut aliquip ex ea commodo consequat.</p>
    <a class="see" href="#">See more</a>
  </article>
  <a class="more" href="#" style="left:211px;top:230px">View All</a>
</section>

<footer class="footer">
  <nav class="foot-links"><a href="#">Home</a><a href="#">K7 Profiles</a><a href="#">Forum</a><a href="#">Advisory</a><a href="#">About</a><a href="#">Contact</a><a href="#">Blog</a></nav>
  <div class="follow">Follow us<div><span></span><span></span><span></span><span></span><span></span></div></div>
  <div class="foot-tab">
    <div class="wordmark">k7ledger</div>
    <small>All rights reserved. 2013</small>
  </div>
</footer>

</body>
</html>
```